Coach company requires modern brochure

We need a brochure designed that shows our various coach services. The aim of the brochure is to attract new business, therefore we need something that is modern, eye-catching and uses a lot of imagery/design rather than being text heavy.

I have all the images that can be sent via dropbox or google drive if you want to request them.

Target Market(s)

Wedding planners, event companies, school business managers, sporting groups

Industry/Entity Type

Tourism

Requirements
Must have
• 4 x a4 pages
• Bold and eye catching cover page

```html
<!DOCTYPE html>
<html lang="en">
<head>
<meta charset="utf-8">
<title>Ridgeline Coaches – Weddings &amp; Events</title>
<link rel="stylesheet" href="https://fonts.googleapis.com/css2?family=Montserrat:wght@500;600;700&family=Open+Sans:ital,wght@1,400&display=swap">
<style>
  :root {
    --heading-blue: #3ea6d4;
    --rule-blue: #a9d9ef;
    --body-text: #2f3a40;
    --band-green: #3cc31f;
    --white: #ffffff;
    --wedding-tone: #dcdedb;
    --event-tone-a: #5d86b8;
    --event-tone-b: #8c9a86;
  }
  * { margin: 0; padding: 0; box-sizing: border-box; }
  html, body { width: 849px; height: 1200px; overflow: hidden; background: var(--white); }
  .page {
    position: relative;
    width: 849px;
    height: 1200px;
    overflow: hidden;
    font-family: "Montserrat", sans-serif;
    color: var(--body-text);
  }
  .page-backdrop {
    position: absolute; inset: 0;
    background: linear-gradient(180deg, #eef2f1 0%, #f5f6f4 40%, #eeede8 100%);
  }
  .section-heading {
    position: absolute;
    font-weight: 700;
    font-size: 31px;
    color: var(--heading-blue);
    line-height: 1;
  }
  .body-copy {
    position: absolute;
    font-weight: 600;
    font-size: 13.7px;
    line-height: 19px;
    text-align: justify;
  }
  .about-copy { left: 51px; top: 115px; width: 749px; }
  .wedding-copy { left: 445px; top: 335px; width: 355px; line-height: 20px; }
  .event-copy { left: 51px; top: 761px; width: 355px; font-size: 14.8px; line-height: 23.4px; }
  .rule {
    position: absolute;
    left: 51px; width: 749px; height: 2px;
    background: var(--rule-blue);
  }
  .photo { position: absolute; }
  .photo-wedding {
    left: 51px; top: 382px; width: 355px; height: 238px;
    background: var(--wedding-tone);
  }
  .photo-event {
    left: 445px; top: 722px; width: 355px; height: 266px;
    background: linear-gradient(180deg, var(--event-tone-a), var(--event-tone-b));
  }
  .quote-band { position: absolute; left: 0; top: 1009px; width: 849px; height: 191px; }
  .quote {
    position: absolute;
    left: 51px; top: 1057px; width: 749px;
    font-family: "Open Sans", sans-serif;
    font-style: italic;
    font-size: 17.6px;
    line-height: 30px;
    color: var(--white);
    text-align: justify;
  }
</style>
</head>
<body>
<main class="page">
  <div class="page-backdrop" role="img" aria-label="Faded beach scene with palm fronds and sand"></div>

  <h2 class="section-heading" style="left:50px; top:68px;">About Us</h2>
  <p class="body-copy about-copy">Ridgeline Coaches is the first choice of wedding, corporate and conference event planners from Caloundra to Gympie and everywhere in between. With a reputation for a reliable, punctual and courteous service, we hand-pick our experienced drivers from the Sunshine Coast region to ensure they maintain the high standards for which we are known. Our fleet of modern, comfortable and well maintained buses are fitted with seat belts and air-conditioning, and some include TV/DVD facilities. Ranging in size from 13 to 57 seat buses, we can deliver on a wide variety of bus charter needs, from small groups of ten through to corporate events requiring the transport of 300 passengers, anywhere on the Sunshine Coast.</p>

  <div class="rule" style="top:297px;"></div>

  <h2 class="section-heading" style="left:50px; top:336px;">Weddings &amp; Events</h2>
  <div class="photo photo-wedding" role="img" aria-label="Photo: wedding reception table setting"></div>
  <p class="body-copy wedding-copy">With its pristine beaches, spectacular mountains and fantastic venues, The Sunshine Coast is fast becoming one of the most popular locations for weddings. Whether you are wanting an outdoor ceremony with your toes in the sand, or under the canopy of a flowering jacaranda in the hinterland, we can transport you and your guests on your special day. Choosing one or a number of our vehicles to transfer guests to your wedding and then to your reception, is the best way to move your family and friends easily while ensuring everything runs to schedule. Why not consider hiring one of our buses to transport your bridal party to different venues on the coast? There’s plenty of space for everyone, including the wedding dress!</p>

  <div class="rule" style="top:695px;"></div>

  <h2 class="section-heading" style="left:50px; top:715px;">Events</h2>
  <p class="body-copy event-copy">Attending a long lunch on a private estate, or hosting a special birthday at one of the Sunshine Coast’s amazing dining venues? If you can’t decide on who should be the designated driver then fear not, we can take the pressure off this decision for you. Our extensive range of fully air-conditioned coaches can fit groups from 4 to 200 so get in touch today and allow us to add the finishing touch to your special event.</p>
  <div class="photo photo-event" role="img" aria-label="Photo: outdoor event marquee with long decorated tables"></div>

  <svg class="quote-band" viewBox="0 0 849 191" aria-hidden="true">
    <polygon points="0,30 188,30 228,0 268,30 849,30 849,191 0,191" fill="var(--band-green)"/>
  </svg>
  <p class="quote">“It was an incredible day and I honestly cannot thank Marco enough for his time and assistance with the co-ordination of the delivery of service and buses on the day. Everything ran seamless which enhanced our clients overall experience. The feedback received to date has been fabulous’ Helena, Brightpath Events.”</p>
</main>
</body>
</html>
```